New business logo / Business Card Design

My company provides Interim Management and consultancy, for Facilities Services. Covers any aspect of facilities management, including M&E, helpdesk, asset management, supplier relationships, catering, cleaning etc. Company provides innovative solutions to exceed client needs, drawing on years of experience. Initial thoughts on logo are attached below. Fits with RAG status on projects, red, amber and green, with logo design colours around moving services from amber to green.

Target Market(s)

Facilities Management clients and service providers

Industry/Entity Type

Business

Contact Information for Business Card

Company Name = k7Rventures Ltd My name on card = Derek Whitcombe, Director Mobile = 07516309842 Email = Derek@k7rventuresltd.co.uk Twitter = @k7Rventures Ltd

Font styles to use
Sans Serif

Colors
f37122
00a990

Requirements
Must have
• Logo to be evident, with some background image in reference to Facilities Management

```html
<!DOCTYPE html>
<html lang="en">
<head>
<meta charset="utf-8">
<title>k7Rventures Ltd – Business Card</title>
<link href="https://fonts.googleapis.com/css2?family=Open+Sans:wght@300;400;700;800&display=swap" rel="stylesheet">
<style>
  :root {
    --backdrop: #6e5539;
    --card-white: #f4f4f4;
    --card-black: #000000;
    --brand-ink: #111111;
    --accent-orange: #e0601a;
    --text-light: #ececec;
    --divider: #8a8a8a;
  }
  * { margin: 0; padding: 0; box-sizing: border-box; }
  html, body {
    width: 1200px; height: 892px; overflow: hidden;
    background: var(--backdrop);
    font-family: "Open Sans", Arial, sans-serif;
  }
  .business-card {
    position: absolute; left: 100px; top: 146px;
    width: 1000px; height: 600px;
    border-radius: 40px; overflow: hidden;
    background: var(--card-black);
    box-shadow: 0 18px 40px rgba(0,0,0,0.45);
  }
  .brand-band {
    position: absolute; left: 0; top: 0; width: 100%; height: 232px;
    background: var(--card-white);
    display: flex; align-items: center; justify-content: flex-end;
    padding-right: 70px;
  }
  .brand-name {
    font-weight: 800; font-size: 104px; letter-spacing: -2px;
    color: var(--brand-ink); line-height: 1;
  }
  .person {
    position: absolute; left: 80px; top: 400px;
  }
  .person-name {
    font-weight: 700; font-size: 44px; color: var(--accent-orange); line-height: 1.1;
  }
  .person-role {
    font-weight: 300; font-size: 34px; color: var(--text-light); margin-top: 4px;
  }
  .divider {
    position: absolute; left: 500px; top: 290px; width: 2px; height: 210px;
    background: var(--divider);
  }
  .contact-list {
    position: absolute; left: 540px; top: 296px; list-style: none;
  }
  .contact-item {
    display: flex; align-items: center; gap: 20px;
    height: 58px; font-size: 30px; font-weight: 400; color: var(--text-light);
  }
  .contact-icon {
    width: 32px; height: 32px; flex: none;
    background: var(--accent-orange); display: block;
  }
</style>
</head>
<body>
  <div class="business-card">
    <header class="brand-band">
      <span class="brand-name">k7Rventures Ltd</span>
    </header>

    <div class="person">
      <div class="person-name">Derek Whitcombe</div>
      <div class="person-role">Director</div>
    </div>

    <div class="divider"></div>

    <ul class="contact-list">
      <li class="contact-item">
        <svg class="contact-icon" viewBox="0 0 32 32" aria-label="Phone">
          <rect width="32" height="32" fill="#e0601a"/>
          <path d="M10 7 l4 0 l1.5 5 l-2.5 2 q2 4 5 5 l2 -2.5 l5 1.5 l0 4 q-1 2 -3 2 q-8 -1 -13 -10 q-1 -3 1 -7z" fill="#000"/>
        </svg>
        <span>07516309842</span>
      </li>
      <li class="contact-item">
        <span class="contact-icon" aria-label="Social handle"></span>
        <span>@k7Rventures Ltd</span>
      </li>
      <li class="contact-item">
        <svg class="contact-icon" viewBox="0 0 32 32" aria-label="Email">
          <rect width="32" height="32" fill="#e0601a"/>
          <rect x="7" y="10" width="18" height="13" fill="none" stroke="#000" stroke-width="2"/>
          <path d="M7 10 L16 18 L25 10" fill="none" stroke="#000" stroke-width="2"/>
        </svg>
        <span>Derek@k7rventuresltd.co.uk</span>
      </li>
    </ul>
  </div>
</body>
</html>
```